Web design

We need the design for the logo and website for a women fashion website. No coding required. The colors used should be neutral (maybe with a light touch of color), the style should be modern, slightly luxurious, not too crowded. The target market is young professionals who love trendy clothes.

Target Market(s)

Young professionals

Industry/Entity Type

Apparel

Number of Pages Required

5+ page

Font styles to use
Sans Serif
Other font styles liked:
• Montserrat, Engravers Gothic, Benton Sans, gotham-book

Colors

Designer to choose colors to be used in the design.

```html
<!DOCTYPE html>
<html lang="en">
<head>
<meta charset="utf-8">
<title>ORAE — Women's Fashion Clothing</title>
<link href="https://fonts.googleapis.com/css2?family=Montserrat:wght@400;500;600;700&display=swap" rel="stylesheet">
<style>
:root{
  --ink:#1d1d1f;
  --muted:#7a7476;
  --gold:#e3b66b;
  --blush:#e8d9d5;
  --blush-deep:#ead0c9;
  --band:#ece2df;
  --news:#d6c4bd;
  --footer:#2e2c2e;
  --price:#d6a89a;
  --white:#fff;
  --line:#cfc7c5;
}
*{margin:0;padding:0;box-sizing:border-box}
html,body{width:1200px;height:4286px;overflow:hidden}
body{position:relative;background:var(--white);font-family:'Montserrat',sans-serif;color:var(--ink)}
.abs{position:absolute}
.display{font-family:'Montserrat',sans-serif;font-weight:600;text-transform:uppercase;letter-spacing:3.5px}
.section-title{position:absolute;left:0;width:1200px;text-align:center;font-size:25px;line-height:34px;color:var(--ink)}
.title-rule{position:absolute;width:90px;height:8px}
.title-rule::before,.title-rule::after{content:"";position:absolute;height:1px;background:#d9b9ae}
.title-rule::before{top:0;left:0;width:90px}
.title-rule::after{top:6px;left:20px;width:50px}

/* hero */
.hero{position:absolute;left:0;top:0;width:1200px;height:771px;background:linear-gradient(100deg,#5c7a96 0%,#8aa2b5 30%,#b69574 60%,#8a5f3c 80%,#6b4a33 100%)}
.hero-shade{position:absolute;inset:0;background:linear-gradient(90deg,rgba(20,25,35,.35),rgba(0,0,0,0) 55%)}
.topbar{position:absolute;top:32px;font-size:14px;color:var(--white)}
.wordmark{position:absolute;font-family:'Montserrat',sans-serif;font-weight:500;color:var(--white);letter-spacing:4px;line-height:1}
.nav a{position:absolute;top:120px;font-size:17px;color:var(--white);text-decoration:none}
.nav .active::after{content:"";position:absolute;left:-4px;right:-4px;bottom:-8px;height:1px;background:var(--white)}
.nav .active::before{content:"";position:absolute;left:20px;right:-12px;top:-10px;height:1px;background:var(--white)}
.hero-brand{position:absolute;left:111px;top:326px;font-size:26px;color:var(--gold);letter-spacing:2px}
.hero-title{position:absolute;left:111px;top:368px;font-size:28px;line-height:36px;color:var(--white);letter-spacing:2.5px;white-space:nowrap}
.hero-copy{position:absolute;left:111px;top:418px;width:480px;font-size:15px;line-height:32px;color:var(--white)}
.btn-shop{position:absolute;left:111px;top:501px;width:154px;height:50px;background:#d8c3b3;color:var(--ink);font-size:16px;font-weight:500;display:flex;align-items:center;justify-content:center}

.dots{position:absolute;left:0;width:1200px;height:20px}

/* shipping */
.ship{position:absolute;width:330px;text-align:center}
.ship-halo{position:absolute;left:75px;top:0;width:180px;height:180px;border-radius:50%;background:#fbf6f5}
.ship-disc{position:absolute;left:96px;top:21px;width:138px;height:138px;border-radius:50%;background:var(--blush-deep);display:flex;align-items:center;justify-content:center}
.ship h3{position:absolute;left:0;top:198px;width:330px;font-size:15px;font-weight:500;line-height:23px;letter-spacing:.5px}
.ship p{position:absolute;left:10px;width:310px;font-size:12px;line-height:22px;color:var(--muted)}

/* product card */
.card{position:absolute;top:1416px;width:235px}
.card .photo{width:235px;height:343px}
.tag{position:absolute;right:8px;top:313px;padding:3px 6px;background:#e9e2d8;font-size:12px;font-weight:500;letter-spacing:.5px}
.swatch{position:absolute;top:355px;width:14px;height:14px}
.fav-line{position:absolute;top:362px;left:210px;width:1px;height:12px;background:var(--line)}
.fav{position:absolute;top:356px;left:218px}
.card .name{position:absolute;left:3px;top:382px;font-size:16px;font-weight:500}
.card .desc{position:absolute;left:3px;top:406px;font-size:12px;color:var(--muted)}
.card .stars{position:absolute;left:3px;top:430px;font-size:12px;color:var(--muted)}
.card .price{position:absolute;left:3px;top:469px;font-size:14px;color:var(--price)}
.sizes{position:absolute;left:3px;top:505px;display:flex}
.sizes span{width:37px;height:28px;border:1px solid var(--line);margin-right:-1px;font-size:13px;display:flex;align-items:center;justify-content:center}
.arrow{position:absolute;top:1560px;width:60px;height:44px}

/* shopping products */
.band{position:absolute;left:0;top:2110px;width:1200px;height:686px;background:var(--band)}
.shop-card{position:absolute;top:2261px;width:236px}
.shop-card .photo{width:236px;height:343px}
.shop-card .cap{margin-top:14px;font-size:16px}
.shop-card .cost{margin-top:8px;font-size:16px;font-weight:600}
.sq-btn{position:absolute;top:2165px;width:44px;height:36px;border:1px solid #c9bdb9;display:flex;align-items:center;justify-content:center}
.pager{position:absolute;left:0;top:2727px;width:1200px;display:flex;justify-content:center;align-items:center;gap:9px;font-size:16px}
.pager span{width:33px;height:30px;border:1px solid #8b8486;display:flex;align-items:center;justify-content:center}
.pager b{font-weight:400;font-size:20px;padding:0 4px}

/* social */
.post{position:absolute;top:2965px;width:318px}
.post .photo{width:318px;height:258px}
.avatar{position:absolute;left:0;top:272px;width:66px;height:66px;border-radius:50%;background:linear-gradient(135deg,#e6ddd4,#a7877a)}
.post .author{position:absolute;left:76px;top:288px;font-size:15px}
.post .handle{position:absolute;left:76px;top:311px;font-size:12px;color:var(--muted)}
.post .badge{position:absolute;right:8px;top:294px;width:24px;height:24px;border-radius:6px;background:#e96a8b}
.post .body{position:absolute;left:0;top:352px;width:300px;font-size:12px;line-height:22px;color:var(--muted)}

/* newsletter */
.news{position:absolute;left:0;top:3533px;width:1200px;height:336px;background:var(--news)}
.news p{position:absolute;left:250px;top:124px;width:700px;text-align:center;font-size:16px;line-height:28px;color:#3d3739}
.news-field{position:absolute;left:276px;top:219px;width:646px;height:62px;border:1px solid #3a3536}
.news-field span{position:absolute;left:14px;top:20px;font-size:16px;color:#3d3739}
.news-btn{position:absolute;right:2px;top:2px;width:183px;height:56px;background:#1c1a1c;color:var(--white);font-size:15px;font-weight:600;display:flex;align-items:center;justify-content:center;letter-spacing:.5px}

/* footer */
.footer{position:absolute;left:0;top:3869px;width:1200px;height:417px;background:var(--footer);color:var(--white)}
.footer h4{position:absolute;font-size:17px;font-weight:600;letter-spacing:.5px}
.footer .link{position:absolute;font-size:14px}
.footer .fine{position:absolute;font-size:13px;line-height:22px}
.social{position:absolute;top:4187px;width:36px;height:36px;border-radius:50%;background:var(--white)}
</style>
</head>
<body>

<!-- HERO -->
<section class="hero" role="img" aria-label="Photo of a woman in a camel trench coat and cap standing in a field of tall dry grass under a blue sky">
  <div class="hero-shade"></div>
</section>
<svg class="abs" style="left:0;top:0" width="1200" height="100" aria-hidden="true">
  <polyline points="0,73 330,73 330,30 540,30" fill="none" stroke="#fff" stroke-width="1.2"/>
  <polyline points="660,30 872,30 872,73 1200,73" fill="none" stroke="#fff" stroke-width="1.2"/>
</svg>
<div class="topbar" style="left:111px">
  <svg width="12" height="12" viewBox="0 0 12 12" style="vertical-align:-1px"><circle cx="6" cy="3.5" r="3" fill="#fff"/><path d="M0 12c0-4 3-5 6-5s6 1 6 5z" fill="#fff"/></svg> My Account
  &nbsp;&nbsp;<svg width="14" height="12" viewBox="0 0 14 12" style="vertical-align:-1px"><path d="M7 11 1.5 5.5a3 3 0 0 1 5.5-3.5 3 3 0 0 1 5.5 3.5z" fill="none" stroke="#fff" stroke-width="1.4"/></svg> Wishlist
</div>
<div class="topbar" style="left:900px">
  <svg width="16" height="13" viewBox="0 0 16 13" style="vertical-align:-1px"><path d="M0 1h3l2 8h9l2-6H4" fill="none" stroke="#fff" stroke-width="1.5"/><circle cx="6" cy="11.5" r="1.3" fill="#fff"/><circle cx="13" cy="11.5" r="1.3" fill="#fff"/></svg> Cart (0)
</div>
<div class="topbar" style="left:1002px;font-size:13px">
  <span style="display:inline-block;width:20px;height:12px;background:linear-gradient(#c8323c 0 50%,#fff 50% 65%,#c8323c 65%);position:relative;vertical-align:-1px"><span style="position:absolute;left:0;top:0;width:9px;height:7px;background:#2f4a8a"></span></span> English
</div>
<div class="wordmark" style="left:500px;top:56px;width:200px;text-align:center;font-size:34px">ORAE</div>
<nav class="nav">
  <a class="active" style="left:369px">Home</a>
  <a style="left:456px">Latest Arrivals</a>
  <a style="left:609px">Clothes</a>
  <a style="left:711px">On Sale</a>
  <a style="left:812px;top:122px"><svg width="16" height="16" viewBox="0 0 16 16"><circle cx="6.5" cy="6.5" r="5" fill="none" stroke="#fff" stroke-width="2"/><path d="M10 10l5 5" stroke="#fff" stroke-width="2.4"/></svg></a>
</nav>
<div class="hero-brand">ORAE</div>
<h1 class="hero-title display">Women's Fashion Clothing</h1>
<p class="hero-copy">Lorem ipsum dolor sit amet, consectetur adipiscing elit, sed do eiusmod tempor incididunt ut labore et dolore</p>
<div class="btn-shop">Shop Now</div>
<svg class="dots" style="top:714px" aria-hidden="true">
  <g stroke="#fff" fill="none" stroke-width="1.3"><line x1="502" y1="10" x2="540" y2="10"/><line x1="678" y1="10" x2="716" y2="10"/>
  <circle cx="553" cy="10" r="7"/><circle cx="581" cy="10" r="7"/><circle cx="609" cy="10" r="7" fill="#fff"/><circle cx="637" cy="10" r="7"/><circle cx="665" cy="10" r="7"/></g>
</svg>

<!-- SHIPPING -->
<h2 class="section-title display" style="top:851px">Shipping Information</h2>
<div class="title-rule" style="left:556px;top:898px"></div>

<div class="ship" style="left:105px;top:943px">
  <div class="ship-halo"></div>
  <div class="ship-disc"><svg width="90" height="90" viewBox="0 0 90 90" fill="none" stroke="#1d1d1f" stroke-width="2"><circle cx="45" cy="45" r="34"/><path d="M22 30c8 2 10 8 16 8s4 10 10 12M50 14c-2 8 6 10 4 18s8 6 14 4M30 66c4-6 12-6 14-12"/><circle cx="64" cy="58" r="8"/><circle cx="64" cy="58" r="3"/></svg></div>
  <h3>SHIPPING WORLDWIDE</h3>
  <p style="top:232px">Lorem ipsum dolor sit amet, adipiscing elit, sed do eiusmod tempor incididunt ut labore aliqua. Ut enim ad minim veniam, quis</p>
</div>
<div class="ship" style="left:435px;top:943px">
  <div class="ship-halo"></div>
  <div class="ship-disc"><svg width="90" height="90" viewBox="0 0 90 90" fill="none" stroke="#1d1d1f" stroke-width="2"><path d="M36 26l22-8 20 8v30l-22 8-20-8z"/><path d="M36 26l20 8 22-8M56 34v30M46 22l20 8v8"/><path d="M12 40h18M16 48h14M10 56h20"/><circle cx="66" cy="52" r="1.5"/><circle cx="71" cy="50" r="1.5"/></svg></div>
  <h3>FREE SHIPPING ON ORDERS<br>GREATER THAN X$,</h3>
  <p style="top:251px">Lorem ipsum dolor sit amet, adipiscing elit, sed do eiusmod tempor incididunt ut labore aliqua. Ut</p>
</div>
<div class="ship" style="left:765px;top:943px">
  <div class="ship-halo"></div>
  <div class="ship-disc"><svg width="90" height="90" viewBox="0 0 90 90" fill="none" stroke="#1d1d1f" stroke-width="2"><path d="M18 40a28 28 0 0 1 50-14M72 50a28 28 0 0 1-50 14"/><path d="M68 16v10H58M22 74V64h10"/><path d="M34 32l12-5 12 5v14l-12 5-12-5z M34 32l12 5 12-5M46 37v14"/><path d="M38 62h2M44 62h2M50 62h2"/></svg></div>
  <h3>30 DAYS RETURN POLICY</h3>
  <p style="top:232px">Lorem ipsum dolor sit amet, adipiscing elit, sed do eiusmod tempor incididunt ut labore aliqua. Ut enim ad minim veniam, quis</p>
</div>

<!-- LATEST COLLECTION -->
<h2 class="section-title display" style="top:1327px">Latest Collection</h2>

<svg class="arrow" style="left:25px" aria-hidden="true"><line x1="0" y1="1" x2="60" y2="1" stroke="#999"/><line x1="0" y1="43" x2="60" y2="43" stroke="#999"/><path d="M38 10 26 22l12 12" fill="none" stroke="#1d1d1f" stroke-width="4"/></svg>
<svg class="arrow" style="left:1110px" aria-hidden="true"><line x1="0" y1="1" x2="60" y2="1" stroke="#999"/><line x1="0" y1="43" x2="60" y2="43" stroke="#999"/><path d="M22 10l12 12-12 12" fill="none" stroke="#1d1d1f" stroke-width="4"/></svg>

<div class="card" style="left:111px">
  <div class="photo" role="img" aria-label="Model in a white blazer with a belt against a grey wall" style="background:linear-gradient(160deg,#8f8a88,#d9d5d3 60%,#efecea)"></div>
  <span class="tag">ON SALE</span>
  <span class="swatch" style="left:3px;background:#8d8d8d"></span><span class="swatch" style="left:24px;background:#4a4a4a"></span>
  <span class="fav-line"></span><svg class="fav" width="14" height="13" viewBox="0 0 14 12"><path d="M7 11 1.5 5.5a3 3 0 0 1 5.5-3.5 3 3 0 0 1 5.5 3.5z" fill="none" stroke="#555" stroke-width="1.2"/></svg>
  <div class="name">Product 1</div><div class="desc">Lorem ipsum dolor sit amet</div><div class="stars">★★★★★ (10)</div><div class="price">$50.00</div>
  <div class="sizes"><span>XL</span><span>L</span><span>M</span></div>
</div>
<div class="card" style="left:358px">
  <div class="photo" role="img" aria-label="Model in a black hat, sunglasses and striped top on a light grey background" style="background:linear-gradient(170deg,#cfd1d2,#b08d72 55%,#e8e4e1)"></div>
  <span class="tag">ON SALE</span>
  <span class="swatch" style="left:3px;background:#8d8d8d"></span><span class="swatch" style="left:24px;background:#4a4a4a"></span>
  <span class="fav-line"></span><svg class="fav" width="14" height="13" viewBox="0 0 14 12"><path d="M7 11 1.5 5.5a3 3 0 0 1 5.5-3.5 3 3 0 0 1 5.5 3.5z" fill="none" stroke="#555" stroke-width="1.2"/></svg>
  <div class="name">Product 2</div><div class="desc">Lorem ipsum dolor sit amet</div><div class="stars">★★★★★ (10)</div><div class="price">$50.00</div>
  <div class="sizes"><span>XL</span><span>L</span><span>M</span></div>
</div>
<div class="card" style="left:604px">
  <div class="photo" role="img" aria-label="Model in an olive green coat and striped trousers on a pink background" style="background:linear-gradient(170deg,#e6c8c2,#a3a77e 55%,#e3c4be)"></div>
  <span class="tag">ON SALE</span>
  <span class="swatch" style="left:3px;background:#8d8d8d"></span><span class="swatch" style="left:24px;background:#4a4a4a"></span>
  <span class="fav-line"></span><svg class="fav" width="14" height="13" viewBox="0 0 14 12"><path d="M7 11 1.5 5.5a3 3 0 0 1 5.5-3.5 3 3 0 0 1 5.5 3.5z" fill="none" stroke="#555" stroke-width="1.2"/></svg>
  <div class="name">Product 3</div><div class="desc">Lorem ipsum dolor sit amet</div><div class="stars">★★★★★ (10)</div><div class="price">$50.00</div>
  <div class="sizes"><span>XL</span><span>L</span><span>M</span></div>
</div>
<div class="card" style="left:850px">
  <div class="photo" role="img" aria-label="Model in a pink top, green trousers and black hat on a blue background" style="background:linear-gradient(170deg,#3fb2d4,#e5318c 45%,#1f9f8a 75%,#36a9cc)"></div>
  <span class="tag">ON SALE</span>
  <span class="swatch" style="left:3px;background:#8d8d8d"></span><span class="swatch" style="left:24px;background:#4a4a4a"></span>
  <span class="fav-line"></span><svg class="fav" width="14" height="13" viewBox="0 0 14 12"><path d="M7 11 1.5 5.5a3 3 0 0 1 5.5-3.5 3 3 0 0 1 5.5 3.5z" fill="none" stroke="#555" stroke-width="1.2"/></svg>
  <div class="name">Product 4</div><div class="desc">Lorem ipsum dolor sit amet</div><div class="stars">★★★★★ (10)</div><div class="price">$50.00</div>
  <div class="sizes"><span>XL</span><span>L</span><span>M</span></div>
</div>

<svg class="dots" style="top:2007px" aria-hidden="true">
  <g stroke="#1d1d1f" fill="none" stroke-width="1.3"><line x1="493" y1="10" x2="533" y2="10"/><line x1="667" y1="10" x2="707" y2="10"/>
  <circle cx="544" cy="10" r="7"/><circle cx="572" cy="10" r="7"/><circle cx="600" cy="10" r="7" fill="#1d1d1f"/><circle cx="628" cy="10" r="7"/><circle cx="656" cy="10" r="7"/></g>
</svg>

<!-- SHOPPING PRODUCTS -->
<section class="band"></section>
<h2 class="abs display" style="left:111px;top:2167px;font-size:25px;line-height:34px">Shopping Products</h2>
<div class="title-rule" style="left:111px;top:2215px"></div>
<div class="sq-btn" style="left:992px"><svg width="10" height="12"><path d="M7 1 2 6l5 5" fill="none" stroke="#555" stroke-width="1.4"/></svg></div>
<div class="sq-btn" style="left:1043px"><svg width="10" height="12"><path d="M3 1l5 5-5 5" fill="none" stroke="#555" stroke-width="1.4"/></svg></div>

<div class="shop-card" style="left:110px"><div class="photo" role="img" aria-label="Model in a dusty pink wrap coat on a grey background" style="background:linear-gradient(160deg,#a9a9ab,#c98579 55%,#9d9b9c)"></div><div class="cap">Lorem ipsum dolor</div><div class="cost">$55.00</div></div>
<div class="shop-card" style="left:358px"><div class="photo" role="img" aria-label="Model in a dusty pink wrap coat, side view, on a grey background" style="background:linear-gradient(160deg,#b0aeaf,#cf8d7f 55%,#a8a6a7)"></div><div class="cap">Lorem ipsum dolor</div><div class="cost">$55.00</div></div>
<div class="shop-card" style="left:604px"><div class="photo" role="img" aria-label="Model in a white blouse and black trousers on a light background" style="background:linear-gradient(170deg,#eeebe8,#f6f2ee 55%,#3b3533 90%)"></div><div class="cap">Lorem ipsum dolor</div><div class="cost">$55.00</div></div>
<div class="shop-card" style="left:852px"><div class="photo" role="img" aria-label="Model in a tan belted jumpsuit against a beige wall" style="background:linear-gradient(160deg,#e3d6c8,#a77a5e 55%,#d9c7b6)"></div><div class="cap">Lorem ipsum dolor</div><div class="cost">$55.00</div></div>

<div class="pager"><b>«</b><span>1</span><span>2</span><span>3</span><span>4</span><span>5</span><b>»</b></div>

<!-- SOCIAL MEDIA POSTS -->
<h2 class="section-title display" style="top:2874px">Social Media Posts</h2>

<article class="post" style="left:113px">
  <div class="photo" role="img" aria-label="Model in white shirt and trousers seated against a beige wall" style="background:linear-gradient(150deg,#d8cbbd,#f1ede8 55%,#cbb9a7)"></div>
  <div class="avatar" role="img" aria-label="Author portrait"></div>
  <div class="author">Nora Ellis</div><div class="handle">Lorem ipsum dolor sit amet</div><span class="badge"></span>
  <p class="body">Lorem ipsum dolor sit amet, consectetur adipiscing elit, sed do eiusmod tempor incididunt ut labore et dolore magna aliqua.</p>
</article>
<article class="post" style="left:441px">
  <div class="photo" role="img" aria-label="Model in an orange coat and beret on a city street" style="background:linear-gradient(160deg,#8e9aa3,#c06c3a 50%,#5b6670)"></div>
  <div class="avatar" role="img" aria-label="Author portrait"></div>
  <div class="author">Nora Ellis</div><div class="handle">Lorem ipsum dolor sit amet</div><span class="badge"></span>
  <p class="body">Lorem ipsum dolor sit amet, consectetur adipiscing elit, sed do eiusmod tempor incididunt ut labore et dolore magna aliqua.</p>
</article>
<article class="post" style="left:769px">
  <div class="photo" role="img" aria-label="Model in a black button dress beside a large green leaf" style="background:linear-gradient(150deg,#dacfc3,#2a2628 50%,#4f5a45 80%,#d4c6b8)"></div>
  <div class="avatar" role="img" aria-label="Author portrait"></div>
  <div class="author">Nora Ellis</div><div class="handle">Lorem ipsum dolor sit amet</div><span class="badge"></span>
  <p class="body">Lorem ipsum dolor sit amet, consectetur adipiscing elit, sed do eiusmod tempor incididunt ut labore et dolore magna aliqua.</p>
</article>

<svg class="dots" style="top:3430px" aria-hidden="true">
  <g stroke="#1d1d1f" fill="none" stroke-width="1.3"><line x1="493" y1="10" x2="533" y2="10"/><line x1="667" y1="10" x2="707" y2="10"/>
  <circle cx="544" cy="10" r="7"/><circle cx="572" cy="10" r="7"/><circle cx="600" cy="10" r="7" fill="#1d1d1f"/><circle cx="628" cy="10" r="7"/><circle cx="656" cy="10" r="7"/></g>
</svg>

<!-- NEWSLETTER -->
<section class="news">
  <h2 class="section-title display" style="top:46px">Subscribe to Newsletter</h2>
  <div class="title-rule" style="left:556px;top:92px"></div>
  <p>Lorem ipsum dolor sit amet, consectetur adipiscing elit, sed do eiusmod tempor incididunt ut labore et dolore magna aliqua. Ut enim ad</p>
  <div class="news-field"><span>Enter Email</span><div class="news-btn">SUBSCRIBE</div></div>
</section>

<!-- FOOTER -->
<footer class="footer">
  <div class="wordmark" style="left:108px;top:73px;font-size:34px">ORAE</div>
  <h4 style="left:111px;top:143px">HELP</h4>
  <span class="link" style="left:111px;top:178px">Returns/exchanges</span>
  <span class="link" style="left:111px;top:210px">Delivery information</span>
  <span class="link" style="left:111px;top:243px">FAQ</span>
  <h4 style="left:300px;top:143px">SHOP</h4>
  <span class="link" style="left:300px;top:178px">Clothes</span>
  <span class="link" style="left:300px;top:210px">Categories</span>
  <h4 style="left:719px;top:143px">SIGN UP FOR ORAE UPDATES</h4>
  <p class="fine" style="left:719px;top:174px;width:370px">Lorem ipsum dolor sit amet, consectetur adipiscing elit, sed do eiusmod tempor incididunt ut labore</p>
  <span class="link" style="left:727px;top:248px;font-size:13px">Enter Email Address</span>
  <svg class="abs" style="left:1060px;top:248px" width="16" height="14"><path d="M1 7h12M8 2l5 5-5 5" fill="none" stroke="#fff" stroke-width="2"/></svg>
  <div class="abs" style="left:719px;top:273px;width:369px;height:1px;background:#8a8688"></div>
  <p class="fine" style="left:111px;top:333px;width:330px">Terms &amp; Conditions, Privacy Policy and @2021 followed by ORAE</p>
</footer>
<span class="social" style="left:837px"></span>
<span class="social" style="left:880px"></span>
<span class="social" style="left:923px"></span>
<span class="social" style="left:966px"></span>
<span class="social" style="left:1009px"></span>
<span class="social" style="left:1052px"></span>

</body>
</html>
```